Business Card Design Project

Looking for a logo and business card for a Real State Business i will be opening. The name is not choosen yet , but will probably be RTV IMOVEIS.
I was thinking black and silver colors, but am open to nice ideas.
I did add a business card that i liked a lot, am looking for something like that, with logo in black or silver in a black card. The logo i was thinking in the letters RTV as i uploaded or something or little and cute buildings or a house...just ideas, can be any nice logo.
Updates

You guys can add other colors if you want, I like colors very "BRIGHT" and "open", like red, pink, strong colors. almost glow in the dark colors. lol

Designers,

I've increased more 88 dollars in the budget for 1st place cause I will want envelope designs... small and big sizes.

So 1st place is now U$248,00. 

No need to send the envelope designs right now... only the business cards designs.

Thank you.

Industry/Entity Type

Business

Requirements
Must have
• Renata Tavares Vilela

www.RTVimoveis-exemplo.com.br

+554188316402

renata@rtvimoveis-exemplo.com.br

```html
<!DOCTYPE html>
<html lang="pt-BR">
<head>
<meta charset="utf-8">
<title>RTV IMOVEIS – Cartão de visita</title>
<link href="https://fonts.googleapis.com/css2?family=Arimo:wght@400&display=swap" rel="stylesheet">
<style>
  :root {
    --stage-red: #ff0000;
    --card-white: #ffffff;
    --card-shadow: #b9c4c8;
    --ink: #111414;
    --band-dark: #1c1e1e;
    --band-mid: #4a4c4c;
    --band-light: #7a7c7c;
    --gold: #e8c21a;
    --gold-pale: #f6e6a0;
  }
  html, body {
    margin: 0;
    padding: 0;
    width: 1200px;
    height: 1100px;
    overflow: hidden;
    background: var(--stage-red);
  }
  .stage {
    display: block;
    width: 1200px;
    height: 1100px;
  }
  .card-text {
    font-family: "Arimo", Arial, sans-serif;
    fill: var(--ink);
  }
  .brand-name { font-size: 44px; letter-spacing: 1px; }
  .person-name { font-size: 38px; }
  .contact-line { font-size: 15px; }
</style>
</head>
<body>
<svg class="stage" width="1200" height="1100" viewBox="0 0 1200 1100" xmlns="http://www.w3.org/2000/svg">
  <defs>
    <clipPath id="front-shape"><rect x="168" y="28" width="852" height="482" rx="45"/></clipPath>
    <clipPath id="back-shape"><rect x="183" y="590" width="844" height="480" rx="45"/></clipPath>
    <linearGradient id="band-front" x1="0" y1="0" x2="1" y2="1">
      <stop offset="0" stop-color="var(--band-light)"/>
      <stop offset="0.45" stop-color="var(--band-mid)"/>
      <stop offset="1" stop-color="var(--band-dark)"/>
    </linearGradient>
    <linearGradient id="band-back" x1="1" y1="1" x2="0" y2="0">
      <stop offset="0" stop-color="var(--band-light)"/>
      <stop offset="0.45" stop-color="var(--band-mid)"/>
      <stop offset="1" stop-color="var(--band-dark)"/>
    </linearGradient>
    <linearGradient id="gold-edge" x1="0" y1="0" x2="1" y2="1">
      <stop offset="0" stop-color="var(--gold)"/>
      <stop offset="0.7" stop-color="var(--gold)"/>
      <stop offset="1" stop-color="var(--gold-pale)"/>
    </linearGradient>
  </defs>

  <!-- Front card -->
  <g class="card card-front">
    <rect class="card-backing" x="205" y="14" width="830" height="476" rx="45" fill="var(--card-shadow)"/>
    <g clip-path="url(#front-shape)">
      <rect x="168" y="28" width="852" height="482" fill="var(--card-white)"/>
      <path class="swoosh-band" role="img" aria-label="Dark swoosh band with fine line texture"
            d="M168,28 L252,28 C300,250 480,420 738,510 L168,510 Z" fill="url(#band-front)"/>
      <path class="swoosh-edge" d="M252,28 C300,250 480,420 738,510" fill="none" stroke="url(#gold-edge)" stroke-width="5"/>
    </g>
    <text class="card-text brand-name" x="706" y="215" text-anchor="middle">RTV IMOVEIS</text>
    <text class="card-text person-name" x="706" y="310" text-anchor="middle">Renata Tavares Vilela</text>
  </g>

  <!-- Back card -->
  <g class="card card-back">
    <rect class="card-backing" x="165" y="605" width="840" height="480" rx="45" fill="var(--card-shadow)"/>
    <g clip-path="url(#back-shape)">
      <rect x="183" y="590" width="844" height="480" fill="var(--card-white)"/>
      <path class="swoosh-band" role="img" aria-label="Dark swoosh band with fine line texture"
            d="M450,590 C700,680 880,850 940,1070 L1027,1070 L1027,590 Z" fill="url(#band-back)"/>
      <path class="swoosh-edge" d="M450,590 C700,680 880,850 940,1070" fill="none" stroke="url(#gold-edge)" stroke-width="5"/>
    </g>
    <text class="card-text contact-line" x="228" y="657">+554188316402</text>
    <text class="card-text brand-name" x="428" y="805" text-anchor="middle">RTV IMOVEIS</text>
    <text class="card-text person-name" x="428" y="893" text-anchor="middle">Renata Tavares Vilela</text>
    <text class="card-text contact-line" x="910" y="1035" text-anchor="end">renata@rtvimoveis-exemplo.com.br</text>
    <text class="card-text contact-line" x="910" y="1058" text-anchor="end">www.RTVimoveis-exemplo.com.br</text>
  </g>
</svg>
</body>
</html>
```